Stationary for Non-Profit Ministry
Jared & Lydia Ministries
Professional
Jared Pelowski
Speaker
4817 W. Harrow Lane Ozark, MO 65894
jaredpl47@mailora.net
www.jared-lydia.org
creatively arranged logo

```html
<!DOCTYPE html>
<html lang="en">
<head>
<meta charset="utf-8">
<title>Jared &amp; Lydia Ministries – Business Card</title>
<link rel="stylesheet" href="https://fonts.googleapis.com/css2?family=Tinos:wght@400;700&display=swap">
<style>
  :root {
    --backdrop-light: #f4f4f4;
    --backdrop-dark: #d9d9d9;
    --card: #ffffff;
    --green: #3f8a1c;
    --green-light: #7dbb3a;
    --green-dark: #2a6510;
    --brand-red: #d4431b;
    --ink: #333333;
  }
  * { box-sizing: border-box; margin: 0; padding: 0; }
  html, body { width: 1200px; height: 945px; overflow: hidden; }
  body {
    background: radial-gradient(ellipse at center, var(--backdrop-light) 30%, var(--backdrop-dark) 100%);
    font-family: "Tinos", "Times New Roman", serif;
    color: var(--ink);
    position: relative;
  }
  .card {
    position: absolute;
    left: 287px;
    width: 626px;
    height: 392px;
    background: var(--card);
    box-shadow: 0 3px 8px rgba(0,0,0,0.22);
    overflow: hidden;
  }
  .card--front { top: 52px; }
  .card--back { top: 509px; }

  .side-tab {
    position: absolute;
    width: 18px;
    background: linear-gradient(90deg, var(--green-dark), var(--green-light));
  }
  .side-tab--left { left: 0; border-radius: 0 14px 14px 0; }
  .side-tab--right { right: 0; border-radius: 14px 0 0 14px; }
  .card--front .side-tab--left { top: 84px; height: 280px; }
  .card--front .side-tab--right { top: 150px; height: 214px; }
  .card--back .side-tab--left { top: 78px; height: 230px; }

  .brand-name {
    position: absolute;
    font-weight: 700;
    color: var(--brand-red);
    white-space: nowrap;
    text-align: center;
  }
  .card--front .brand-name { left: 50px; top: 100px; width: 300px; font-size: 23px; }
  .card--back .brand-name { left: 0; top: 200px; width: 626px; font-size: 36px; }

  .name-bar {
    position: absolute;
    left: 332px; top: 132px;
    width: 294px; height: 52px;
    background: linear-gradient(90deg, var(--green-light), var(--green-dark) 60%);
    border-radius: 4px 0 0 4px;
    color: #fff;
    font-size: 32px;
    font-weight: 400;
    line-height: 52px;
    padding-left: 18px;
    white-space: nowrap;
  }
  .role {
    position: absolute;
    right: 26px; top: 190px;
    font-size: 18px;
  }
  .contact {
    position: absolute;
    right: 38px; top: 270px;
    text-align: right;
    font-size: 15px;
    line-height: 20px;
    list-style: none;
    white-space: nowrap;
  }
  .contact .sep { padding: 0 6px; }

  .footer-band {
    position: absolute;
    left: 0; bottom: 0;
    width: 626px; height: 64px;
  }
  .footer-band svg { display: block; }
  .footer-url {
    position: absolute;
    left: 0; bottom: 16px; width: 626px;
    text-align: center;
    color: #fff;
    font-size: 19px;
  }
</style>
</head>
<body>

  <section class="card card--front">
    <div class="side-tab side-tab--left"></div>
    <div class="side-tab side-tab--right"></div>

    <p class="brand-name">Jared &amp; Lydia Ministries</p>

    <h1 class="name-bar">Jared Pelowski</h1>
    <p class="role">Speaker</p>

    <ul class="contact">
      <li>E-mail: jaredpl47@mailora.net</li>
      <li>Tool Free # 800-555-0142<span class="sep">|</span>Cell # 904-555-0187</li>
      <li>Address: 4817 W. Harrow Lane, Ozark, MO 65894</li>
      <li>Web: www.jared-lydia.org</li>
    </ul>
  </section>

  <section class="card card--back">
    <div class="side-tab side-tab--left"></div>

    <p class="brand-name">Jared &amp; Lydia Ministries</p>

    <div class="footer-band">
      <svg width="626" height="64" viewBox="0 0 626 64">
        <defs>
          <linearGradient id="bandFill" x1="0" y1="0" x2="1" y2="0">
            <stop offset="0" stop-color="#2a6510"/>
            <stop offset="0.5" stop-color="#3f8a1c"/>
            <stop offset="1" stop-color="#7dbb3a"/>
          </linearGradient>
        </defs>
        <path d="M0 12 H560 Q626 12 626 -20 V64 H0 Z" fill="url(#bandFill)"/>
      </svg>
    </div>
    <p class="footer-url">www.jared-lydia.org</p>
  </section>

</body>
</html>
```